Re-Design the flow of the Keystride Principles

The keystride principle is a 10 step model that helps teams/organizations become high performing. Attached the model which i created. I love the design as it is but i used a template i don't owe the rights of so i would like to use this platform to see what you can come up with the redesign this flow while keeping the key elements in place. I like the flow, i like the cleanness and i like it to be compact.

Target Market(s)

Organizational change / Leadership/ Consultancy

Industry/Entity Type

Leadership

Requirements
Must have
• Keep as much as possible the flow and feel of the attached
Nice to have
• -Maybe some twist in how the different parts connect (not a must)
Should not have
• Less or more steps than added in the attached file

```html
<!DOCTYPE html>
<html lang="en">
<head>
<meta charset="utf-8">
<title>Keystride Principles – 10 Step Model</title>
<link href="https://fonts.googleapis.com/css2?family=Archivo+Black&family=Roboto:wght@400;500;700&display=swap" rel="stylesheet">
<style>
  :root {
    --blue-dark: #0652a0;
    --blue-mid: #33a5d8;
    --blue-light: #cfe6f4;
    --title-dark: #0b4f9c;
    --white: #ffffff;
  }
  html, body {
    margin: 0;
    padding: 0;
    width: 1200px;
    height: 841px;
    overflow: hidden;
    background: var(--white);
  }
  .model { display: block; width: 1200px; height: 841px; }

  .seg { stroke: var(--white); stroke-width: 5; stroke-linejoin: miter; }
  .seg--dark { fill: var(--blue-dark); }
  .seg--mid { fill: var(--blue-mid); }
  .seg--light { fill: var(--blue-light); }

  .hub--dark { fill: var(--blue-dark); }
  .hub--mid { fill: var(--blue-mid); }
  .hub-orbit { fill: none; stroke-width: 2; stroke-dasharray: 3 7; stroke-linecap: round; }
  .hub-orbit--dark { stroke: var(--blue-dark); }
  .hub-orbit--mid { stroke: var(--blue-mid); }
  .hub-label {
    font-family: "Roboto", Arial, sans-serif;
    font-weight: 500;
    font-size: 22px;
    fill: var(--white);
    text-anchor: middle;
  }

  .step-label {
    font-family: "Roboto", Arial, sans-serif;
    font-size: 12.5px;
    text-anchor: middle;
  }
  .step-label--on-dark { fill: var(--white); }
  .step-label--on-light { fill: var(--blue-dark); }

  .badge--on-dark circle { fill: var(--white); }
  .badge--on-dark text { fill: var(--blue-dark); }
  .badge--on-light circle { fill: var(--blue-dark); }
  .badge--on-light text { fill: var(--white); }
  .badge text {
    font-family: "Roboto", Arial, sans-serif;
    font-weight: 700;
    font-size: 13px;
    text-anchor: middle;
  }

  .restart-label {
    font-family: "Roboto", Arial, sans-serif;
    font-weight: 500;
    font-size: 15px;
    fill: var(--white);
    text-anchor: middle;
  }

  .outcome-title {
    font-family: "Roboto", Arial, sans-serif;
    font-weight: 500;
    font-size: 12.5px;
    fill: var(--blue-dark);
    text-anchor: middle;
  }
  .outcome-list {
    font-family: "Roboto", Arial, sans-serif;
    font-size: 11.5px;
    fill: var(--blue-dark);
  }
  .bullet { fill: var(--blue-dark); }

  .theme-title {
    font-family: "Archivo Black", "Arial Black", sans-serif;
    font-size: 40px;
    text-anchor: middle;
  }
  .theme-title--dark { fill: var(--title-dark); }
  .theme-title--mid { fill: var(--blue-mid); }
</style>
</head>
<body>
<svg class="model" viewBox="0 0 1200 841" xmlns="http://www.w3.org/2000/svg" aria-label="Keystride Principles ten step model">
  <defs>
    <path id="arc-human" d="M81.9,349.7 A264,264 0 0 1 558.6,308"/>
    <path id="arc-self" d="M47.9,364.4 A292,292 0 0 0 304.6,730.9"/>
    <path id="arc-unleash" d="M563.1,465.1 A288,288 0 0 0 1136.9,465.1"/>
    <path id="arc-restart-left-1" d="M367.4,616.1 A180,180 0 0 0 496.9,507.4"/>
    <path id="arc-restart-left-2" d="M375.7,655.2 A220,220 0 0 0 534,522.4"/>
    <path id="arc-restart-right-1" d="M687.6,303.7 A212,212 0 0 1 894.1,232.6"/>
    <path id="arc-restart-right-2" d="M718.2,329.4 A172,172 0 0 1 885.8,271.8"/>
  </defs>

  <!-- Return arrows -->
  <path class="seg seg--dark restart restart--right" d="M915,198.5 A250,250 0 0 0 645.2,296.6 L628.8,285.1 L664.5,379.7 L751.7,371.2 L735.3,359.7 A140,140 0 0 1 886.2,304.8 Z"/>
  <path class="seg seg--dark restart restart--left" d="M567.8,517.3 A250,250 0 0 1 373.4,686.2 L376.9,705.9 L309.6,633.9 L350.8,558.2 L354.3,577.9 A140,140 0 0 0 463.1,483.3 Z"/>

  <!-- Foundation loop: steps 1–6 -->
  <g class="loop loop--foundation">
    <path class="seg seg--light" d="M295.2,687.6 A250,250 0 0 1 140.8,603.4 L224,531.5 A140,140 0 0 0 310.5,578.6 Z"/>
    <path class="seg seg--dark" d="M140.8,603.4 A250,250 0 0 1 80,438.7 L190,439.3 A140,140 0 0 0 224,531.5 Z"/>
    <path class="seg seg--mid" d="M80,438.7 A250,250 0 0 1 142.8,274.4 L225.1,347.2 A140,140 0 0 0 190,439.3 Z"/>
    <path class="seg seg--light" d="M142.8,274.4 A250,250 0 0 1 298.2,192 L312.2,301.1 A140,140 0 0 0 225.1,347.2 Z"/>
    <path class="seg seg--dark" d="M298.2,192 A250,250 0 0 1 469.1,232.3 L407.9,323.7 A140,140 0 0 0 312.2,301.1 Z"/>
    <path class="seg seg--mid" d="M469.1,232.3 A250,250 0 0 1 571.5,375.3 L465.2,403.8 A140,140 0 0 0 407.9,323.7 Z"/>
  </g>

  <!-- Bridge: step 7 -->
  <path class="seg seg--light bridge" d="M465.2,403.8 L571.5,375.3 L608.5,375.3 L714.8,403.8 A140,140 0 0 0 714.8,476.2 L608.5,504.7 L571.5,504.7 L465.2,476.2 A140,140 0 0 0 465.2,403.8 Z"/>

  <!-- Excellence loop: steps 8–10 and outcome -->
  <g class="loop loop--excellence">
    <path class="seg seg--mid" d="M744.4,666.6 A250,250 0 0 1 608.5,504.7 L714.8,476.2 A140,140 0 0 0 790.8,566.9 Z"/>
    <path class="seg seg--dark" d="M955.6,666.6 A250,250 0 0 1 744.4,666.6 L790.8,566.9 A140,140 0 0 0 909.2,566.9 Z"/>
    <path class="seg seg--mid" d="M1100,440 A250,250 0 0 1 955.6,666.6 L909.2,566.9 A140,140 0 0 0 990,440 Z"/>
    <path class="seg seg--light outcome" d="M975,434 L975,262 L950,262 L1045,110 L1140,262 L1115,262 L1115,434 Z"/>
  </g>

  <!-- Hubs -->
  <g class="hub hub--foundation-group">
    <circle class="hub-orbit hub-orbit--dark" cx="330" cy="440" r="126"/>
    <circle class="hub--dark" cx="330" cy="440" r="112"/>
    <text class="hub-label"><tspan x="330" y="420">Capabilities</tspan><tspan x="330" y="448">Driving a Solid</tspan><tspan x="330" y="476">Foundation</tspan></text>
  </g>
  <g class="hub hub--excellence-group">
    <circle class="hub-orbit hub-orbit--mid" cx="850" cy="440" r="126"/>
    <circle class="hub--mid" cx="850" cy="440" r="112"/>
    <text class="hub-label"><tspan x="850" y="420">Capabilities</tspan><tspan x="850" y="448">Maximizing</tspan><tspan x="850" y="476">Excellence</tspan></text>
  </g>

  <!-- Step 1 -->
  <g class="step">
    <g class="badge badge--on-light"><circle cx="237" cy="573" r="12"/><text x="237" y="577.5">1</text></g>
    <text class="step-label step-label--on-light"><tspan x="237" y="603">Discover your</tspan><tspan x="237" y="618">purpose. Why</tspan><tspan x="237" y="633">Do you exist?</tspan></text>
  </g>
  <!-- Step 2 -->
  <g class="step">
    <g class="badge badge--on-dark"><circle cx="147" cy="462" r="12"/><text x="147" y="466.5">2</text></g>
    <text class="step-label step-label--on-dark"><tspan x="147" y="492">Identify</tspan><tspan x="147" y="507">Purpose</tspan><tspan x="147" y="522">Activators</tspan><tspan x="147" y="537">(Vision)</tspan></text>
  </g>
  <!-- Step 3 -->
  <g class="step">
    <g class="badge badge--on-dark"><circle cx="148" cy="334" r="12"/><text x="148" y="338.5">3</text></g>
    <text class="step-label step-label--on-dark"><tspan x="148" y="364">Develop a</tspan><tspan x="148" y="379">Master plan</tspan><tspan x="148" y="394">(strategy)</tspan></text>
  </g>
  <!-- Step 4 -->
  <g class="step">
    <g class="badge badge--on-light"><circle cx="239" cy="226" r="12"/><text x="239" y="230.5">4</text></g>
    <text class="step-label step-label--on-light"><tspan x="239" y="256">Cultivate</tspan><tspan x="239" y="271">Psychological</tspan><tspan x="239" y="286">Safety &amp;</tspan><tspan x="239" y="301">Ownership</tspan></text>
  </g>
  <!-- Step 5 -->
  <g class="step">
    <g class="badge badge--on-dark"><circle cx="375" cy="216" r="12"/><text x="375" y="220.5">5</text></g>
    <text class="step-label step-label--on-dark"><tspan x="375" y="245">Tap into peoples</tspan><tspan x="375" y="260">Purpose &amp; Passion</tspan><tspan x="375" y="275">(intrinsic</tspan><tspan x="375" y="290">motivation)</tspan></text>
  </g>
  <!-- Step 6 -->
  <g class="step">
    <g class="badge badge--on-dark"><circle cx="489" cy="286" r="12"/><text x="489" y="290.5">6</text></g>
    <text class="step-label step-label--on-dark"><tspan x="489" y="316">Unlock culture</tspan><tspan x="489" y="331">of personal</tspan><tspan x="489" y="346">growth &amp;</tspan><tspan x="489" y="361">development</tspan></text>
  </g>
  <!-- Step 7 -->
  <g class="step">
    <g class="badge badge--on-light"><circle cx="590" cy="400" r="12"/><text x="590" y="404.5">7</text></g>
    <text class="step-label step-label--on-light"><tspan x="590" y="430">Prioritize</tspan><tspan x="590" y="445">Feedback &amp;</tspan><tspan x="590" y="460">Transparency</tspan></text>
  </g>
  <!-- Step 8 -->
  <g class="step">
    <g class="badge badge--on-dark"><circle cx="701" cy="525" r="12"/><text x="701" y="529.5">8</text></g>
    <text class="step-label step-label--on-dark"><tspan x="701" y="555">Empower the</tspan><tspan x="701" y="570">community from</tspan><tspan x="701" y="585">bottom-up</tspan></text>
  </g>
  <!-- Step 9 -->
  <g class="step">
    <g class="badge badge--on-dark"><circle cx="850" cy="598" r="12"/><text x="850" y="602.5">9</text></g>
    <text class="step-label step-label--on-dark"><tspan x="850" y="627">Put excellent (team)</tspan><tspan x="850" y="642">performance in</tspan><tspan x="850" y="657">the spotlight</tspan></text>
  </g>
  <!-- Step 10 -->
  <g class="step">
    <g class="badge badge--on-dark"><circle cx="1014" cy="505" r="12"/><text x="1014" y="509.5">10</text></g>
    <text class="step-label step-label--on-dark"><tspan x="1014" y="535">Monitor</tspan><tspan x="1014" y="550">engagement</tspan><tspan x="1014" y="565">Real-time</tspan></text>
  </g>

  <!-- Restart labels -->
  <text class="restart-label"><textPath href="#arc-restart-left-1" startOffset="50%">(RE)START HERE</textPath></text>
  <text class="restart-label"><textPath href="#arc-restart-left-2" startOffset="50%">(RE)INVENT HERE</textPath></text>
  <text class="restart-label"><textPath href="#arc-restart-right-1" startOffset="50%">(RE)START HERE</textPath></text>
  <text class="restart-label"><textPath href="#arc-restart-right-2" startOffset="50%">(RE)INVENT HERE</textPath></text>

  <!-- Outcome -->
  <text class="outcome-title"><tspan x="1045" y="198">Reaching Full</tspan><tspan x="1045" y="214">Potential Of</tspan><tspan x="1045" y="230">People &amp;</tspan><tspan x="1045" y="246">Organization</tspan></text>
  <g class="outcome-list">
    <circle class="bullet" cx="990" cy="279" r="3.5"/>
    <circle class="bullet" cx="990" cy="311" r="3.5"/>
    <circle class="bullet" cx="990" cy="343" r="3.5"/>
    <circle class="bullet" cx="990" cy="375" r="3.5"/>
    <text><tspan x="999" y="283">Productivity upto</tspan><tspan x="999" y="297">800%</tspan><tspan x="999" y="315">Employee</tspan><tspan x="999" y="329">engagement &gt;90%</tspan><tspan x="999" y="347">Max discretionary</tspan><tspan x="999" y="361">effort gap</tspan><tspan x="999" y="379">High resilience to</tspan><tspan x="999" y="393">change</tspan></text>
  </g>

  <!-- Theme titles -->
  <text class="theme-title theme-title--dark"><textPath href="#arc-human" startOffset="50%">Human Experience</textPath></text>
  <text class="theme-title theme-title--dark"><textPath href="#arc-self" startOffset="50%">Self Direction</textPath></text>
  <text class="theme-title theme-title--mid"><textPath href="#arc-unleash" startOffset="50%">Unleash Engangement</textPath></text>
</svg>
</body>
</html>
```